Bookmark Design

We would like to design a book mark with logos of our two business and a quote.

One side with the quote "The first wealth is health" - Tobias Quill Harrow and the two logos.

The back side has the two logos with its respective phone numbers and a common address (this is to be advised to the winner of the project).

```html
<!DOCTYPE html>
<html lang="en">
<head>
<meta charset="utf-8">
<title>Bookmark – Brackenridge Clinic &amp; Harbourview Dental</title>
<link rel="stylesheet" href="https://fonts.googleapis.com/css2?family=Tinos:ital,wght@0,400;0,700;1,400&display=swap">
<style>
  :root {
    --backdrop: #c9cbcc;
    --kraft: #a68f6f;
    --frame-green: #5fae4e;
    --clinic-blue: #1f4f9e;
    --string: #4a4a4a;
    --ink-light: #ffffff;
  }
  * { margin: 0; padding: 0; box-sizing: border-box; }
  html, body {
    width: 758px; height: 1200px; overflow: hidden;
    background: var(--backdrop);
  }
  .canvas {
    position: relative; width: 758px; height: 1200px;
    font-family: "Tinos", "Times New Roman", serif;
  }
  .strings { position: absolute; inset: 0; pointer-events: none; z-index: 2; }
  .bookmark {
    position: absolute; top: 230px; width: 306px; height: 885px;
    background: var(--kraft);
    border-radius: 153px 153px 6px 6px;
  }
  .bookmark--back { left: 50px; }
  .bookmark--front { left: 421px; }
  .bookmark__hole {
    position: absolute; top: 12px; left: 50%; width: 14px; height: 14px;
    margin-left: -7px; border-radius: 50%; background: var(--backdrop);
  }
  .clinic-mark {
    position: absolute; top: 150px; left: 0; right: 0;
    display: flex; flex-direction: column; align-items: center; gap: 14px;
  }
  .clinic-mark__dot {
    width: 104px; height: 104px; border-radius: 50%;
    border: 4px solid var(--clinic-blue);
  }
  .clinic-mark__name {
    color: var(--clinic-blue); font-weight: 700; font-size: 26px; letter-spacing: 0.5px;
  }
  .info-frame {
    position: absolute; top: 372px; left: 20px; width: 266px; height: 270px;
    border: 2px solid var(--frame-green);
    display: flex; flex-direction: column; align-items: center; justify-content: center;
    color: var(--ink-light); text-align: center;
  }
  .contact { font-weight: 700; font-size: 20px; line-height: 1.3; }
  .quote__text { font-weight: 700; font-size: 52px; line-height: 1.1; }
  .quote__author { font-style: italic; font-size: 18px; margin-top: 14px; }
  .dental-mark {
    position: absolute; top: 690px; left: 0; right: 0;
    display: flex; flex-direction: column; align-items: center;
    color: var(--ink-light); font-weight: 700; font-size: 38px; line-height: 1.1;
    text-align: center;
  }
</style>
</head>
<body>
<div class="canvas">
  <div class="bookmark bookmark--back">
    <span class="bookmark__hole"></span>
    <div class="clinic-mark">
      <span class="clinic-mark__dot"></span>
      <span class="clinic-mark__name">BRACKENRIDGE</span>
    </div>
    <div class="info-frame">
      <p class="contact">Address<br>Contact :<br>000 0000 000</p>
    </div>
    <div class="dental-mark">
      <span>Harbourview</span>
      <span>Dental</span>
    </div>
  </div>

  <div class="bookmark bookmark--front">
    <span class="bookmark__hole"></span>
    <div class="clinic-mark">
      <span class="clinic-mark__dot"></span>
      <span class="clinic-mark__name">BRACKENRIDGE</span>
    </div>
    <div class="info-frame quote">
      <p class="quote__text">The first<br>wealth<br>is health</p>
      <p class="quote__author">Tobias Quill Harrow</p>
    </div>
    <div class="dental-mark">
      <span>Harbourview</span>
      <span>Dental</span>
    </div>
  </div>

  <svg class="strings" width="758" height="1200" viewBox="0 0 758 1200">
    <g fill="none" stroke="var(--string)" stroke-width="2.5" stroke-linecap="round">
      <path d="M203 249 C 185 200, 150 90, 165 40 C 175 10, 225 8, 238 35 C 252 70, 225 190, 203 249"/>
      <path d="M574 249 C 556 200, 521 90, 536 40 C 546 10, 596 8, 609 35 C 623 70, 596 190, 574 249"/>
    </g>
  </svg>
</div>
</body>
</html>
```